Top notch designer needed for world class recruitment app!

We need an app design for an Amsterdam-based company that is about to change the way we find new jobs. The idea is not to show the company and job title as everyone does, but only a 5 sentence summary of the job. The user slides though the jobs and eventuelly finds a shortlist of his best matching jobs.

Winning designers supplies 2 designs, that have contain the core of our business idea (see screenshots attached):

Screenshot 1, A job description done in 5 bulletpoints (6-9 words).

example:

- Lead 20 enthusiastic workers
- Coordinate between production department and development team
- Improve current processes
- Maintain relations with supplier
- Lot of focus on personal development

Screenshot 2 should be a shortlist/favourites

The shortlists shows around 5 jobs with job title, company logo, number of days the
vacancy will stay available, and how well the job matches to your profile (preferably by means of a visual indicator).

Target Market(s)

Young professionals looking for a job. Well educated withless than 10 years work experience. Typical user would be someone who uses workvine regularly.

Industry/Entity Type

Business

Requirements
Must have
• The 2 screenshots (see attachment) with awesome look and feel, with content as described in attachment.. The winning designs should (also) be available in PSD format, or less preferably in PNG.

Nice to have
• Inspiration:
Flicko: simple and clear slide throughs (yes/no)
Workvine: start screen (professional and stylish), vacancy banner (visual, but not distracting)
Roomly: combination of playfull and professional design
Should not have
• We like to have it as visual as possible, but visuals cannot directly relate to the job (because we cannot match a visual to every job). So should be something 'business like' or 'city life'.

When a user clicks on the 'i (more info)' button the user can see info like job title, company name, location. Its important that this info is not shown in screenshot 1.

```html
<!DOCTYPE html>
<html lang="en">
<head>
<meta charset="utf-8">
<title>Shortlist</title>
<link href="https://fonts.googleapis.com/css2?family=Open+Sans:wght@300;400;600;700&display=swap" rel="stylesheet">
<style>
  :root {
    --status-bg: #2f9e8a;
    --header-bg: #3fbba4;
    --title-teal: #47b7a3;
    --row-white: #ffffff;
    --row-grey: #f4f4f4;
    --divider: #e6e6e6;
    --muted: #9a9a9a;
    --company-text: #5a5a5a;
    --bar-track: #e3e3e3;
    --avatar-tone: #c9b39e;
  }
  * { box-sizing: border-box; margin: 0; padding: 0; }
  html, body { width: 690px; height: 1200px; overflow: hidden; background: #ffffff; }
  body { font-family: "Open Sans", Arial, sans-serif; }

  .app { width: 690px; height: 1200px; overflow: hidden; position: relative; background: var(--row-white); }

  .status-bar {
    height: 36px; background: var(--status-bg); color: #e8f7f3;
    display: flex; align-items: center; justify-content: space-between;
    padding: 0 20px; font-size: 17px; font-weight: 400;
  }
  .status-left, .status-right { display: flex; align-items: center; gap: 8px; width: 200px; }
  .status-right { justify-content: flex-end; }
  .status-time { font-weight: 600; }

  .nav-bar {
    height: 95px; background: var(--header-bg);
    display: flex; align-items: center; justify-content: space-between; padding: 0 36px;
    color: #ffffff;
  }
  .nav-title { font-size: 34px; font-weight: 400; letter-spacing: 0.3px; }
  .avatar {
    width: 58px; height: 58px; border-radius: 50%;
    background: radial-gradient(circle at 50% 40%, #e2d2c2, var(--avatar-tone));
    border: 3px solid rgba(255,255,255,0.85);
  }

  .job-list { list-style: none; }
  .job-row {
    height: 141px; display: flex; justify-content: space-between; align-items: flex-start;
    padding: 30px 44px 0 50px; border-bottom: 1px solid var(--divider);
  }
  .job-row:nth-child(even) { background: var(--row-grey); }

  .job-title { font-size: 27px; font-weight: 400; color: var(--title-teal); margin-bottom: 14px; line-height: 1.3; }
  .company { font-size: 18px; font-weight: 600; color: var(--company-text); line-height: 1.3; }

  .match { width: 176px; text-align: right; padding-top: 6px; }
  .days-left { font-size: 16px; color: var(--muted); margin-bottom: 10px; }
  .match-bar { height: 7px; background: var(--bar-track); border-radius: 4px; overflow: hidden; }
  .match-fill {
    height: 100%; border-radius: 4px;
    background: linear-gradient(90deg, #e53935 0%, #f7a21b 40%, #f2d52a 62%, #7ccc4e 100%);
    background-size: 176px 100%;
  }
  .match-score { font-size: 12px; color: var(--muted); margin-top: 8px; }
</style>
</head>
<body>
<div class="app">
  <div class="status-bar">
    <div class="status-left">
      <svg width="62" height="12" viewBox="0 0 62 12" aria-hidden="true">
        <g fill="#e8f7f3"><circle cx="6" cy="6" r="5"/><circle cx="18" cy="6" r="5"/><circle cx="30" cy="6" r="5"/><circle cx="42" cy="6" r="5"/></g>
        <circle cx="54" cy="6" r="4.3" fill="none" stroke="#e8f7f3" stroke-width="1.4"/>
      </svg>
      <span>CARRIO</span>
      <svg width="20" height="15" viewBox="0 0 20 15" aria-hidden="true">
        <path d="M10 14 L2 6 A11 11 0 0 1 18 6 Z" fill="#e8f7f3"/>
      </svg>
    </div>
    <span class="status-time">4:21 PM</span>
    <div class="status-right">
      <span>100%</span>
      <svg width="34" height="16" viewBox="0 0 34 16" aria-hidden="true">
        <rect x="1" y="1" width="28" height="14" rx="3" fill="none" stroke="#e8f7f3" stroke-width="1.5"/>
        <rect x="3.5" y="3.5" width="23" height="9" rx="1.5" fill="#e8f7f3"/>
        <rect x="30.5" y="5" width="2.5" height="6" rx="1" fill="#e8f7f3"/>
      </svg>
    </div>
  </div>

  <header class="nav-bar">
    <svg class="menu-icon" width="30" height="22" viewBox="0 0 30 22" aria-label="Menu">
      <g fill="#ffffff"><rect y="0" width="30" height="4" rx="1"/><rect y="9" width="30" height="4" rx="1"/><rect y="18" width="30" height="4" rx="1"/></g>
    </svg>
    <h1 class="nav-title">Shortlist</h1>
    <div class="avatar" role="img" aria-label="User profile photo"></div>
  </header>

  <ul class="job-list">
    <li class="job-row">
      <div><h2 class="job-title">Front End Engineer</h2><p class="company">Brightdesk</p></div>
      <div class="match"><p class="days-left">15 days left</p><div class="match-bar"><div class="match-fill" style="width:75%"></div></div><p class="match-score">75% match</p></div>
    </li>
    <li class="job-row">
      <div><h2 class="job-title">Lead Developer</h2><p class="company">Nodmedia</p></div>
      <div class="match"><p class="days-left">7 days left</p><div class="match-bar"><div class="match-fill" style="width:100%"></div></div><p class="match-score">100% match</p></div>
    </li>
    <li class="job-row">
      <div><h2 class="job-title">Wordpress Developer</h2><p class="company">Townlink</p></div>
      <div class="match"><p class="days-left">12 days left</p><div class="match-bar"><div class="match-fill" style="width:25%"></div></div><p class="match-score">25% match</p></div>
    </li>
    <li class="job-row">
      <div><h2 class="job-title">Front End Engineer</h2><p class="company">Brightdesk</p></div>
      <div class="match"><p class="days-left">15 days left</p><div class="match-bar"><div class="match-fill" style="width:75%"></div></div><p class="match-score">75% match</p></div>
    </li>
    <li class="job-row">
      <div><h2 class="job-title">Lead Developer</h2><p class="company">Nodmedia</p></div>
      <div class="match"><p class="days-left">7 days left</p><div class="match-bar"><div class="match-fill" style="width:100%"></div></div><p class="match-score">100% match</p></div>
    </li>
    <li class="job-row">
      <div><h2 class="job-title">Wordpress Developer</h2><p class="company">Townlink</p></div>
      <div class="match"><p class="days-left">12 days left</p><div class="match-bar"><div class="match-fill" style="width:25%"></div></div><p class="match-score">25% match</p></div>
    </li>
    <li class="job-row">
      <div><h2 class="job-title">Front End Engineer</h2><p class="company">Brightdesk</p></div>
      <div class="match"><p class="days-left">15 days left</p><div class="match-bar"><div class="match-fill" style="width:75%"></div></div><p class="match-score">75% match</p></div>
    </li>
    <li class="job-row">
      <div><h2 class="job-title">Lead Developer</h2><p class="company">Nodmedia</p></div>
      <div class="match"><p class="days-left">7 days left</p><div class="match-bar"><div class="match-fill" style="width:100%"></div></div><p class="match-score">100% match</p></div>
    </li>
  </ul>
</div>
</body>
</html>
```